Ovelin Watch app inspired by the Perch Thermostat

Wendle allows you to control your Perch Thermostat from your Ovelin Orbit device (Zentrix Watch).
The UI consists of two screens, phone and device, and the design will resemble the Perch look and feel (do not exactly copy, I need something that looks similar). The thermostat control will be front and center, with a white background and blue highlights.
A logo is also needed (custom typography is a plus).

My app is live in the Ovelin Bazaar Market at:
shop.zentrix.example/store/apps/details?id=com.brightforgeworks.wendle

The app currently supports the following devices:

The KV Qband:
https://shop.zentrix.example/store/devices/details?id=kv_q_band_black

The Tarvolo Rook Pulse:
https://shop.zentrix.example/store/devices/details?id=tarvolo_rook_pulse_black

Target Market(s)

Zentrix Watch wearers who have a Perch at home.

Industry/Entity Type

Ovelin

Colors
33a6d7
0555a3
3176b5
fefefe
85acd3
ffffff
cee9f5
cedeec
fbc994

Requirements
Must have
• Two screen designs:
• 1. A 1080 x 1920 px layout for ovelin phones.
• 2. A 320 x 320 px layout for Ovelin Orbit devices (please Zentrix "KV Q Band" or "Tarvolo Rook Pulse" for a visual of the devices I support).
• Design should resemble the Perch experience at perch.example. Using similar fonts, theme and shapes is a must. Please don't copy and paste elements. I need your interpretation of the UI, not the exact same elements from Perch.
• Please look at the screenshots of the Perch Ovelin app for inspiration:
• https://shop.zentrix.example/store/apps/details?id=com.perchworks.ovelin&hl=en
Nice to have
• The project consists of two rather simple layouts, so I'm asking for a logo for my app as well.
Should not have
• No black/dark backgrounds, no square buttons. Please approach the Perch look and feel as much as possible, especially in the QBand design.
• This should go without saying but:
• DO NOT copy paste elements from the Perch page. DO NOT plagiarize other peoples logos or artwork.
• Only original design work will win the contest.

```html
<!DOCTYPE html>
<html lang="en">
<head>
<meta charset="utf-8">
<title>Wendle – thermostat app concept</title>
<link rel="stylesheet" href="https://fonts.googleapis.com/css2?family=Roboto:wght@400;700&display=swap">
<style>
  :root{
    --board:#a9abad;
    --brand:#33a6d7;
    --brand-deep:#1f8fc4;
    --ring:#5cbbe4;
    --tick:#cee9f5;
    --white:#ffffff;
    --online:#8dc63f;
    --photo-light:#ece9e4;
    --photo-mid:#cfc8bf;
    --photo-dark:#6e665e;
  }
  *{box-sizing:border-box;margin:0;padding:0}
  html,body{width:1200px;height:1200px;overflow:hidden}
  body{position:relative;background:var(--board);font-family:"Roboto",Arial,sans-serif;color:var(--brand)}
  .board-top{position:absolute;left:0;top:0;width:1200px;height:558px;background:var(--board)}
  .brand-badge{position:absolute;left:60px;top:42px;width:384px;height:384px;border-radius:50%;background:var(--white);display:flex;flex-direction:column;align-items:center;justify-content:center;gap:56px;padding-top:30px}
  .brand-mark{width:72px;height:72px;border:4px solid var(--brand)}
  .brand-name{font-weight:700;font-size:52px;color:var(--brand);line-height:1}
  .phone-screen{position:absolute;top:54px;width:268px;height:474px;background:var(--white)}
  .phone-screen.first{left:614px}
  .phone-screen.second{left:916px}
  .app-bar{height:26px;background:var(--brand);display:flex;align-items:center;padding:0 8px;gap:6px;color:var(--white);font-size:10px;font-weight:700}
  .app-bar .app-dot{width:16px;height:16px;border-radius:50%;background:var(--white)}
  .app-bar .app-title{flex:1}
  .app-bar .menu{width:3px;height:12px;background:radial-gradient(circle,var(--white) 1.4px,transparent 1.6px) 0 0/3px 4px repeat-y}
  .dial{position:absolute;left:34px;top:111px;width:200px;height:230px}
  .room{position:absolute;left:0;right:0;top:333px;text-align:center;font-size:17px;line-height:20px;color:var(--brand)}
  .status{position:absolute;left:0;right:0;top:353px;text-align:center;font-size:15px;line-height:18px;color:var(--online)}
  .watch-tile{position:absolute;left:428px;top:370px;width:156px;height:156px;background:var(--white);border:4px solid var(--brand)}
  .watch-tile svg{width:100%;height:100%}
  .scene{position:absolute;left:0;top:558px;width:1200px;height:642px;background:linear-gradient(160deg,var(--photo-light) 0%,var(--photo-mid) 55%,var(--photo-dark) 100%)}
  .scene-logo{position:absolute;left:900px;top:640px;width:260px;display:flex;flex-direction:column;align-items:center;gap:30px}
  .scene-logo .brand-mark{width:66px;height:66px}
  .scene-logo .brand-name{font-size:44px}
</style>
</head>
<body>
  <section class="board-top">
    <div class="brand-badge">
      <div class="brand-mark"></div>
      <div class="brand-name">Wendle</div>
    </div>

    <div class="watch-tile">
      <svg viewBox="0 0 156 156" aria-label="Watch screen, 60 degrees, target 78">
        <polyline points="66,30 78,19 90,30" fill="none" stroke="var(--brand)" stroke-width="5"/>
        <polyline points="66,126 78,137 90,126" fill="none" stroke="var(--brand)" stroke-width="5"/>
        <circle cx="74" cy="76" r="41" fill="var(--ring)"/>
        <circle cx="74" cy="76" r="36" fill="none" stroke="var(--tick)" stroke-width="6" stroke-dasharray="1 2.5" opacity=".7"/>
        <circle cx="74" cy="76" r="30" fill="var(--brand)"/>
        <path d="M50 52 A34 34 0 0 1 74 42" fill="none" stroke="var(--white)" stroke-width="5"/>
        <text x="74" y="88" text-anchor="middle" font-family="Roboto, Arial, sans-serif" font-weight="700" font-size="32" fill="var(--white)">60</text>
        <circle cx="135" cy="74" r="10" fill="var(--white)" stroke="var(--brand)" stroke-width="1.5"/>
        <text x="135" y="78" text-anchor="middle" font-family="Roboto, Arial, sans-serif" font-weight="700" font-size="10" fill="var(--brand)">78</text>
      </svg>
    </div>

    <div class="phone-screen first">
      <div class="app-bar"><span class="app-dot"></span><span class="app-title">Wendle</span><span class="menu"></span></div>
      <svg class="dial" viewBox="-100 -115 200 230" aria-label="Dial set to 75, target 70">
        <circle cx="0" cy="-90" r="11" fill="var(--white)" stroke="var(--brand)" stroke-width="1.5"/>
        <text x="0" y="-85" text-anchor="middle" font-family="Roboto, Arial, sans-serif" font-weight="700" font-size="13" fill="var(--brand)">70</text>
        <circle cx="0" cy="10" r="88" fill="var(--ring)"/>
        <circle cx="0" cy="10" r="78" fill="none" stroke="var(--tick)" stroke-width="14" stroke-dasharray="1 3" opacity=".7"/>
        <circle cx="0" cy="10" r="64" fill="var(--brand)"/>
        <path d="M0 -68 A78 78 0 0 1 42 -56" fill="none" stroke="var(--white)" stroke-width="8"/>
        <polyline points="-9,-25 0,-34 9,-25" fill="none" stroke="var(--white)" stroke-width="3"/>
        <text x="0" y="29" text-anchor="middle" font-family="Roboto, Arial, sans-serif" font-weight="700" font-size="54" fill="var(--white)">75</text>
        <polyline points="-9,45 0,54 9,45" fill="none" stroke="var(--white)" stroke-width="3"/>
      </svg>
      <div class="room">Living Room</div>
      <div class="status">Online</div>
    </div>

    <div class="phone-screen second">
      <div class="app-bar"><span class="app-dot"></span><span class="app-title">Wendle</span><span class="menu"></span></div>
      <svg class="dial" viewBox="-100 -115 200 230" aria-label="Dial set to 60, target 78">
        <circle cx="0" cy="-90" r="11" fill="var(--white)" stroke="var(--brand)" stroke-width="1.5"/>
        <text x="0" y="-85" text-anchor="middle" font-family="Roboto, Arial, sans-serif" font-weight="700" font-size="13" fill="var(--brand)">78</text>
        <circle cx="0" cy="10" r="88" fill="var(--ring)"/>
        <circle cx="0" cy="10" r="78" fill="none" stroke="var(--tick)" stroke-width="14" stroke-dasharray="1 3" opacity=".7"/>
        <circle cx="0" cy="10" r="64" fill="var(--brand)"/>
        <path d="M-58 -40 A78 78 0 0 1 0 -68" fill="none" stroke="var(--white)" stroke-width="8"/>
        <polyline points="-9,-25 0,-34 9,-25" fill="none" stroke="var(--white)" stroke-width="3"/>
        <text x="0" y="29" text-anchor="middle" font-family="Roboto, Arial, sans-serif" font-weight="700" font-size="54" fill="var(--white)">60</text>
        <polyline points="-9,45 0,54 9,45" fill="none" stroke="var(--white)" stroke-width="3"/>
      </svg>
      <div class="room">Living Room</div>
      <div class="status">Online</div>
    </div>
  </section>

  <section class="scene" role="img" aria-label="Photo: a hand holding a phone running the Wendle app beside a cup of coffee on a café table"></section>
  <div class="scene-logo">
    <div class="brand-mark"></div>
    <div class="brand-name">Wendle</div>
  </div>
</body>
</html>
```